SunMeadow Yoga Website Design

Business Logo - attached
5 pages being:
Home
About
Classes
Blog
Contact

Would like Scrolling webpage and yoga symbols to be used.

Must have's being:
Easy to navigate, Text needs to be able to be edited/updated, Enquire Now Links, More Information Links, be a secure site, SEO,

Please refer to attached document for the information for the body of the website.

Target Market(s)

Educators, Community Service, Health and Wellbeing, Mental Health

Industry/Entity Type

Yoga

Coding

Coded - Design and coding required

Number of Pages Required

5+ page

Font styles to use
Other font styles liked:
• Bella Bold BC

Colors
0094D4
00A9DD
6FCCEA
C7EBF8
E9F6FB
6B429C
8869AF
B7A5CE
E3DAEB
F3F0F8

Requirements
Must have
• Easy to navigate, Text needs to be able to be edited/updated, Enquire Now Links, More Information Links, be a secure site, SEO,
Nice to have
• Scrolling webpage, yoga symbols

```html
<!DOCTYPE html>
<html lang="en">
<head>
<meta charset="utf-8">
<title>SunMeadow Yoga</title>
<link href="https://fonts.googleapis.com/css2?family=Inter:wght@400;700&display=swap" rel="stylesheet">
<style>
  :root {
    --purple-deep: #6B429C;
    --purple-mid: #8869AF;
    --purple-soft: #B7A5CE;
    --lilac: #E1DAEA;
    --lilac-pale: #EDEBF2;
    --blue-mat: #6FCCEA;
    --ink: #111111;
    --white: #ffffff;
  }
  * { margin: 0; padding: 0; box-sizing: border-box; }
  html, body { width: 1200px; height: 853px; overflow: hidden; background: var(--white); }
  body { font-family: "Inter", Arial, sans-serif; position: relative; }

  .site-header { position: absolute; top: 0; left: 0; width: 1200px; height: 108px; background: var(--white); }
  .brand { position: absolute; left: 40px; top: 40px; display: flex; align-items: center; gap: 6px;
    color: var(--purple-mid); font-size: 13px; font-weight: 400; text-decoration: none; }
  .brand-dot { width: 10px; height: 10px; border-radius: 50%; background: var(--purple-mid); }
  .main-nav a { position: absolute; top: 47px; font-size: 13.3px; color: var(--purple-mid); text-decoration: none; }
  .login-btn { position: absolute; left: 1002px; top: 41px; width: 142px; height: 29px; border-radius: 15px;
    background: var(--purple-mid); color: var(--white); font-size: 13.3px; display: flex;
    align-items: center; justify-content: center; text-decoration: none; }

  .hero-shapes { position: absolute; top: 0; left: 0; }

  .hero-copy { position: absolute; left: 127px; top: 172px; width: 450px; }
  .hero-title { font-size: 60px; font-weight: 700; color: var(--purple-deep); letter-spacing: -0.5px;
    line-height: 1; margin-bottom: 26px; }
  .hero-copy p { font-size: 13.3px; line-height: 23.3px; color: var(--ink); margin-bottom: 23.3px; }

  .art { position: absolute; }
  .art-yogi { left: 637px; top: 225px; width: 330px; height: 392px; border-radius: 40% 40% 6px 6px;
    background: linear-gradient(180deg, #c7b6dc 0%, #a590c6 55%, var(--blue-mat) 85%); }
  .art-plant-right { left: 929px; top: 287px; width: 204px; height: 305px; border-radius: 50% 50% 20px 20px;
    background: linear-gradient(180deg, var(--purple-mid), #a896b6); }
  .art-plant-left { left: 0; top: 475px; width: 88px; height: 248px; border-radius: 0 40px 14px 0;
    background: linear-gradient(180deg, #7a5ba8, #b1a3b7); }
</style>
</head>
<body>
  <header class="site-header">
    <a class="brand" href="#"><span class="brand-dot"></span>SunMeadow Yoga</a>
    <nav class="main-nav">
      <a href="#" style="left:325px">Home</a>
      <a href="#" style="left:429px">About</a>
      <a href="#" style="left:533px">Classes</a>
      <a href="#" style="left:649px">Blog</a>
      <a href="#" style="left:744px">Contact</a>
    </nav>
    <a class="login-btn" href="#">Log in</a>
  </header>

  <svg class="hero-shapes" width="1200" height="853" viewBox="0 0 1200 853" aria-hidden="true">
    <path fill="#EDEBF2" d="M0 108 H1200 V600 C1000 700 800 760 560 777 C330 790 120 740 0 700 Z"/>
    <path fill="#E1DAEA" d="M0 108 H160 C120 180 125 260 180 330 C235 400 110 520 100 600 C92 660 60 700 0 705 Z"/>
    <path fill="#E1DAEA" d="M630 108 H910 C930 200 935 300 945 380 C960 420 1080 370 1200 360 V370 C1200 600 1050 750 880 748 C700 745 595 640 600 520 C605 400 700 330 690 250 C680 180 640 150 630 108 Z"/>
    <path fill="#E1DAEA" d="M1050 121 C1110 115 1170 160 1200 190 V260 C1170 290 1110 315 1060 305 C1010 295 1000 240 1005 190 C1010 145 1025 124 1050 121 Z"/>
  </svg>

  <section class="hero-copy">
    <h1 class="hero-title">SunMeadow yoga</h1>
    <p>SunMeadow Yoga believe that you are never too young to benefit from and fall in love with yoga.</p>
    <p>My aim is to EMPOWER kids and teens to thrive by teaching life skills in Yoga, Mindfulness and Breathing techniques to deal with daily challenges and big emotions.</p>
    <p>SunMeadow Yoga gives kids an opportunity to enjoy and experience yoga for themselves and primarily focuses on programs for Schools, Pre Schools and Early Learning Centres, Private Classes, Sporting Clubs, Martial Arts Schools, Scout Groups and Occupational Therapy Centres just to name a few.</p>
    <p>All classes are age appropriate and encourage children’s natural drive to learn, move, and be creative.</p>
  </section>

  <div class="art art-plant-right" role="img" aria-label="Illustration of a potted plant with broad purple leaves"></div>
  <div class="art art-yogi" role="img" aria-label="Illustration of a woman holding a dancer yoga pose on a blue mat"></div>
  <div class="art art-plant-left" role="img" aria-label="Illustration of a potted plant with spotted purple leaves"></div>
</body>
</html>
```